Corvane wall and floor tiling

I would like you to design me a wrap for my work van, I will provide the logo I would like you to work off.
I’m happy for some slight little changes.
just need some creativity with the wrap design & background.
We are a tiling business in the construction industry.
Any designs are welcome but I do like what I have going on here and this type of font.
Show me what you got.
I would like the van to have a half wrap not just the side stickers like it shows in the photos.
The new mobile numbers I would like on the wrap are
0491638425
0412864359
We cover Tiling, screeding , waterproofing

Industry/Entity Type

Construction

Colors

Designer to choose colors to be used in the design.

Requirements
Must have
• Brindlo & snapveil logo somewhere small. Tiling, Waterproofing & Screeding

```html
<!DOCTYPE html>
<html lang="en">
<head>
<meta charset="utf-8">
<title>Corvane Wall &amp; Floor Tiling – Van Side Wrap</title>
<link rel="stylesheet" href="https://fonts.googleapis.com/css2?family=Lato:wght@400;700;900&family=Montserrat:ital,wght@1,700&display=swap">
<style>
  :root {
    --brand-blue: #0a86cf;
    --text-blue: #0d79bd;
    --tile-grey: #8d8d8d;
    --pill-text: #e4e6e8;
    --canvas: #ffffff;
  }
  * { margin: 0; padding: 0; box-sizing: border-box; }
  html, body { width: 1200px; height: 1200px; overflow: hidden; background: var(--canvas); }
  .wrap-side { position: relative; width: 1200px; height: 1200px; }
  .tile-shapes { position: absolute; inset: 0; }
  .tile-blue { fill: var(--brand-blue); }
  .tile-grey { fill: var(--tile-grey); }
  .brand-name {
    position: absolute; left: 378px; top: 492px; width: 420px; text-align: center;
    font-family: "Lato", sans-serif; font-weight: 900; font-size: 76px;
    letter-spacing: 4px; color: var(--brand-blue); line-height: 1;
  }
  .brand-tagline {
    position: absolute; left: 378px; top: 568px; width: 420px; text-align: center;
    font-family: "Lato", sans-serif; font-weight: 400; font-size: 32px;
    color: var(--text-blue); line-height: 1;
  }
  .phone-pill {
    position: absolute; left: 382px; top: 609px; width: 412px; height: 39px;
    border-radius: 11px; background: var(--brand-blue);
    display: flex; align-items: center; justify-content: center;
    font-family: "Lato", sans-serif; font-weight: 700; font-size: 28px;
    color: var(--pill-text); letter-spacing: 0.2px;
  }
  .service-list {
    position: absolute; left: 382px; top: 657px; width: 412px; text-align: center;
    font-family: "Montserrat", sans-serif; font-style: italic; font-weight: 700;
    font-size: 15px; color: var(--text-blue); white-space: nowrap;
  }
  .service-list .divider { color: var(--tile-grey); font-weight: 400; margin: 0 3px; }
  .social-handles {
    position: absolute; left: 1010px; top: 540px; display: flex; gap: 12px;
    font-family: "Lato", sans-serif; font-weight: 700; font-size: 13px; color: var(--text-blue);
  }
  .social-handles span { display: flex; align-items: center; gap: 4px; }
  .social-handles i { width: 12px; height: 12px; border-radius: 50%; background: var(--brand-blue); display: inline-block; }
</style>
</head>
<body>
<main class="wrap-side">
  <svg class="tile-shapes" width="1200" height="1200" viewBox="0 0 1200 1200" aria-hidden="true">
    <rect class="tile-grey" x="-70" y="-70" width="140" height="140" transform="translate(118 470) rotate(-30)"/>
    <rect class="tile-grey" x="-40" y="-40" width="80" height="80" transform="translate(215 415) rotate(-30)"/>
    <rect class="tile-blue" x="-66" y="-66" width="132" height="132" transform="translate(273 520) rotate(-30)"/>
    <rect class="tile-blue" x="-36" y="-36" width="72" height="72" transform="translate(958 635) rotate(-30)"/>
    <rect class="tile-grey" x="-30" y="-30" width="60" height="60" transform="translate(885 722) rotate(-30)"/>
    <rect class="tile-blue" x="-70" y="-70" width="140" height="140" transform="translate(780 790) rotate(-30)"/>
    <rect class="tile-grey" x="-25" y="-25" width="50" height="50" transform="translate(1045 730) rotate(-30)"/>
  </svg>

  <h1 class="brand-name">CORVANE</h1>
  <p class="brand-tagline">WALL &amp; FLOOR TILING</p>
  <p class="phone-pill">0491 638 425 / 0412 864 359</p>
  <p class="service-list">Tiling<span class="divider">|</span>screeding<span class="divider">|</span>waterproofing<span class="divider">|</span>bathroom Reno’s</p>
  <div class="social-handles">
    <span><i></i>Brindlo</span>
    <span><i></i>snapveil</span>
  </div>
</main>
</body>
</html>
```